5x5 Pop Up Display, Company Logo With Text and Graphics for Tradeshow Display

Design for a 5ft x 5ft pop up trade show display that will sit on top of a table. I usually prefer clean, somewhat minimalist designs. We are a food service company but it's not a requirement to have photos of food. Design elements should compliment the table cloth that we have for the booth. The below may be included depending on the design aesthetic.
Service Provided: Daily Meal Service, Kitchen Management
"Nationwide Footprint"
"Grassroots Service"
"Fresh Scratch Cooking"
"Custom Menus"
"Made To Order Meals"

```html
<!DOCTYPE html>
<html lang="en">
<head>
<meta charset="utf-8">
<title>Hearth Table – 5x5 Pop Up Display</title>
<link rel="stylesheet" href="https://fonts.googleapis.com/css2?family=Saira+Condensed:wght@600&display=swap">
<style>
:root{
  --page:#ffffff;
  --panel:#eef0f0;
  --band-grey:#d6d6d2;
  --green:#3f7a3a;
  --ink:#2b2b2b;
  --white:#ffffff;
  --flame:#e8a33a;
  --dots:#555555;
}
*{box-sizing:border-box;margin:0;padding:0}
html,body{width:1200px;height:2468px;overflow:hidden;background:var(--page)}
body{position:relative;font-family:"Saira Condensed",Arial Narrow,sans-serif;font-weight:600;color:var(--ink)}
.display{position:absolute;left:340px;width:520px;height:520px;background:var(--panel);box-shadow:4px 5px 8px rgba(0,0,0,.35);overflow:hidden}
.display--one{top:110px}
.display--two{top:1000px}
.display--three{top:1815px}
.divider{position:absolute;left:275px;width:690px;border-top:3px dotted var(--dots)}
.divider--one{top:848px}
.divider--two{top:1665px}
.brand-band{position:absolute;left:170px;top:0;width:180px;height:250px;background:var(--band-grey)}
.footer-band{position:absolute;left:0;bottom:0;width:100%;height:52px;background:var(--band-grey);display:flex;align-items:center;justify-content:space-between;padding:0 26px 0 58px;font-size:18px;letter-spacing:.5px}
.display--three .brand-band,.display--three .footer-band{background:var(--green)}
.display--three .footer-band,.display--three .brand-name{color:var(--white)}
.contact{display:flex;align-items:center;gap:6px}
.contact svg{width:18px;height:18px;fill:currentColor}
.brand{position:absolute;left:170px;top:26px;width:180px;display:flex;align-items:center;justify-content:center;gap:6px}
.brand-name{font-size:30px;line-height:.9;text-align:center;color:var(--ink);letter-spacing:1px}
.brand-mark{width:14px;height:14px;border-radius:50%;background:var(--flame)}
.tagline{position:absolute;left:66px;top:96px;width:388px;height:30px;border:1.5px dashed var(--green);border-radius:5px;background:var(--panel);display:flex;align-items:center;justify-content:center;font-size:18px;letter-spacing:1.2px;color:var(--ink)}
.hero{position:absolute;left:157px;top:152px;width:210px;height:210px;border-radius:50%;background:radial-gradient(circle,#3f7a3a 0 30%,#ececec 32%,#ffffff 70%,#d9d9d9 100%);box-shadow:0 4px 10px rgba(0,0,0,.3)}
.service{position:absolute;width:46px;height:46px;border-radius:50%;background:var(--green)}
.label{position:absolute;font-size:13.5px;line-height:1;letter-spacing:.6px;text-align:center;color:var(--ink)}
</style>
</head>
<body>

<section class="display display--one">
  <div class="brand-band"></div>
  <div class="brand"><div class="brand-name">HEARTH<br>TABLE</div><span class="brand-mark"></span></div>
  <div class="tagline">SERVING GREAT FOOD TO GREAT CHAPTERS.</div>
  <div class="hero" role="img" aria-label="White plate holding a phone showing the ordering app"></div>
  <div class="service" role="img" aria-label="Plates icon" style="left:109px;top:153px"></div>
  <div class="label" style="left:20px;top:164px;width:84px">DAILY MEAL<br>SERVICE</div>
  <div class="service" role="img" aria-label="Kitchen icon" style="left:99px;top:243px"></div>
  <div class="label" style="left:14px;top:254px;width:80px;text-align:left">MANAGING<br>KITCHEN</div>
  <div class="service" role="img" aria-label="Cooking icon" style="left:137px;top:325px"></div>
  <div class="label" style="left:115px;top:375px;width:90px">FRESH<br>SCRATCH<br>COOKING</div>
  <div class="service" role="img" aria-label="Globe icon" style="left:239px;top:372px"></div>
  <div class="label" style="left:212px;top:422px;width:100px">NATIONWIDE<br>FOOTPRINT</div>
  <div class="service" role="img" aria-label="Community icon" style="left:339px;top:325px"></div>
  <div class="label" style="left:312px;top:375px;width:100px">GRASSROOTS<br>SERVICE</div>
  <div class="service" role="img" aria-label="Menu icon" style="left:377px;top:243px"></div>
  <div class="label" style="left:428px;top:254px;width:80px;text-align:left">CUSTOM<br>MENUS</div>
  <div class="service" role="img" aria-label="Order icon" style="left:369px;top:153px"></div>
  <div class="label" style="left:424px;top:157px;width:70px">MADE TO<br>ORDER<br>MEALS</div>
  <div class="footer-band">
    <span class="contact"><svg viewBox="0 0 24 24"><circle cx="12" cy="12" r="12"/><path d="M8 6l2 0 1 3-1.5 1a8 8 0 0 0 4.5 4.5l1-1.5 3 1 0 2c0 1-1 2-2 2A11 11 0 0 1 6 8c0-1 1-2 2-2z" fill="var(--panel)"/></svg>555.010.4821</span>
    <span class="contact"><svg viewBox="0 0 24 16"><path d="M0 0h24v16H0z"/><path d="M1 1l11 8 11-8" stroke="var(--panel)" stroke-width="1.6" fill="none"/></svg>INFO@HEARTHTABLE.COM</span>
  </div>
</section>

<div class="divider divider--one"></div>

<section class="display display--two">
  <div class="brand-band"></div>
  <div class="brand"><div class="brand-name">HEARTH<br>TABLE</div><span class="brand-mark"></span></div>
  <div class="tagline">SERVING GREAT FOOD TO GREAT CHAPTERS.</div>
  <div class="hero" role="img" aria-label="White plate holding a phone showing the ordering app"></div>
  <div class="service" role="img" aria-label="Plates icon" style="left:109px;top:153px"></div>
  <div class="label" style="left:20px;top:164px;width:84px">DAILY MEAL<br>SERVICE</div>
  <div class="service" role="img" aria-label="Kitchen icon" style="left:99px;top:243px"></div>
  <div class="label" style="left:14px;top:254px;width:80px;text-align:left">MANAGING<br>KITCHEN</div>
  <div class="service" role="img" aria-label="Cooking icon" style="left:137px;top:325px"></div>
  <div class="label" style="left:115px;top:375px;width:90px">FRESH<br>SCRATCH<br>COOKING</div>
  <div class="service" role="img" aria-label="Globe icon" style="left:239px;top:372px"></div>
  <div class="label" style="left:212px;top:422px;width:100px">NATIONWIDE<br>FOOTPRINT</div>
  <div class="service" role="img" aria-label="Community icon" style="left:339px;top:325px"></div>
  <div class="label" style="left:312px;top:375px;width:100px">GRASSROOTS<br>SERVICE</div>
  <div class="service" role="img" aria-label="Menu icon" style="left:377px;top:243px"></div>
  <div class="label" style="left:428px;top:254px;width:80px;text-align:left">CUSTOM<br>MENUS</div>
  <div class="service" role="img" aria-label="Order icon" style="left:369px;top:153px"></div>
  <div class="label" style="left:424px;top:157px;width:70px">MADE TO<br>ORDER<br>MEALS</div>
  <div class="footer-band">
    <span class="contact"><svg viewBox="0 0 24 24"><circle cx="12" cy="12" r="12"/><path d="M8 6l2 0 1 3-1.5 1a8 8 0 0 0 4.5 4.5l1-1.5 3 1 0 2c0 1-1 2-2 2A11 11 0 0 1 6 8c0-1 1-2 2-2z" fill="var(--panel)"/></svg>555.010.4821</span>
    <span class="contact"><svg viewBox="0 0 24 16"><path d="M0 0h24v16H0z"/><path d="M1 1l11 8 11-8" stroke="var(--panel)" stroke-width="1.6" fill="none"/></svg>INFO@HEARTHTABLE.COM</span>
  </div>
</section>

<div class="divider divider--two"></div>

<section class="display display--three">
  <div class="brand-band"></div>
  <div class="brand"><div class="brand-name">HEARTH<br>TABLE</div><span class="brand-mark"></span></div>
  <div class="tagline">SERVING GREAT FOOD TO GREAT CHAPTERS.</div>
  <div class="hero" role="img" aria-label="White plate holding a phone showing the ordering app"></div>
  <div class="service" role="img" aria-label="Plates icon" style="left:109px;top:153px"></div>
  <div class="label" style="left:20px;top:164px;width:84px">DAILY MEAL<br>SERVICE</div>
  <div class="service" role="img" aria-label="Kitchen icon" style="left:99px;top:243px"></div>
  <div class="label" style="left:14px;top:254px;width:80px;text-align:left">MANAGING<br>KITCHEN</div>
  <div class="service" role="img" aria-label="Cooking icon" style="left:137px;top:325px"></div>
  <div class="label" style="left:115px;top:375px;width:90px">FRESH<br>SCRATCH<br>COOKING</div>
  <div class="service" role="img" aria-label="Globe icon" style="left:239px;top:372px"></div>
  <div class="label" style="left:212px;top:422px;width:100px">NATIONWIDE<br>FOOTPRINT</div>
  <div class="service" role="img" aria-label="Community icon" style="left:339px;top:325px"></div>
  <div class="label" style="left:312px;top:375px;width:100px">GRASSROOTS<br>SERVICE</div>
  <div class="service" role="img" aria-label="Menu icon" style="left:377px;top:243px"></div>
  <div class="label" style="left:428px;top:254px;width:80px;text-align:left">CUSTOM<br>MENUS</div>
  <div class="service" role="img" aria-label="Order icon" style="left:369px;top:153px"></div>
  <div class="label" style="left:424px;top:157px;width:70px">MADE TO<br>ORDER<br>MEALS</div>
  <div class="footer-band">
    <span class="contact"><svg viewBox="0 0 24 24"><circle cx="12" cy="12" r="12"/><path d="M8 6l2 0 1 3-1.5 1a8 8 0 0 0 4.5 4.5l1-1.5 3 1 0 2c0 1-1 2-2 2A11 11 0 0 1 6 8c0-1 1-2 2-2z" fill="var(--green)"/></svg>555.010.4821</span>
    <span class="contact"><svg viewBox="0 0 24 16"><path d="M0 0h24v16H0z"/><path d="M1 1l11 8 11-8" stroke="var(--green)" stroke-width="1.6" fill="none"/></svg>INFO@HEARTHTABLE.COM</span>
  </div>
</section>

</body>
</html>
```